eBook Lumio

I currently use the free eBook app Lumio avail from tolvex

I would like an app to be developed the same but with the following options

But I would like an option in my book listing to mark off the books I've already read.

Maybe also an option to rate the book as well.

Option to choose different bookshelves
Like a nice white beachy looking one
Dark timber very formal
Colourful funky

Target Market(s)

All readers who love to carry all there books with them

Requirements
Must have
• Similar bookshelf look
Either be able to list books or show thumbnail of books
Epub and PDF format
Able to sort by Titles, Author or Catergories
Must have a search field
Nice to have
• Option to choose different bookshelves
Dark timber very formal
Colourful funky

```html
<!DOCTYPE html>
<html lang="en">
<head>
<meta charset="utf-8">
<title>Shelfwise – Library</title>
<link rel="stylesheet" href="https://fonts.googleapis.com/css2?family=Libre+Baskerville&family=Open+Sans:wght@400;600&display=swap">
<style>
  :root {
    --page-bg: #0d0d0e;
    --header-top: #3b3e44;
    --header-bottom: #25272b;
    --toolbar: #2e3136;
    --pill: #24262a;
    --pill-edge: #3f4248;
    --tab-divider: #1f2124;
    --text-light: #f2f2f2;
    --text-muted: #c9ccd1;
    --icon-muted: #6f737a;
    --accent: #f07b1c;
    --shelf-back: #33363c;
    --shelf-ledge-top: #5a5e66;
    --shelf-ledge-bottom: #2d3035;
    --ribbon: #c8242c;
    --ribbon-dot: #5a0c10;
    --cover-cream: #efe3c2;
    --cover-maroon: #8a2134;
    --cover-green: #2f6a34;
    --cover-ink: #3a2a1a;
  }
  * { box-sizing: border-box; margin: 0; padding: 0; }
  html, body { width: 1200px; height: 2333px; overflow: hidden; background: var(--page-bg); }
  body { position: relative; font-family: "Open Sans", Arial, sans-serif; }

  .app-screen {
    position: absolute; left: 30px; top: 320px; width: 1140px; height: 1692px;
    background: linear-gradient(#2c2f34, #1f2125);
    overflow: hidden;
  }
  .app-header {
    position: absolute; left: 0; top: 0; width: 100%; height: 165px;
    background: linear-gradient(var(--header-top), var(--header-bottom));
    border-bottom: 2px solid #1a1b1e;
    display: flex; align-items: center; justify-content: center;
  }
  .app-name { color: var(--text-light); font-size: 64px; font-weight: 600; letter-spacing: -1px; }

  .toolbar {
    position: absolute; left: 0; top: 165px; width: 100%; height: 200px;
    background: var(--toolbar);
    border-top: 1px solid #3e4147;
  }
  .view-list { position: absolute; left: 96px; top: 250px; }
  .view-grid { position: absolute; left: 186px; top: 254px; }
  .search-field {
    position: absolute; left: 260px; top: 239px; width: 620px; height: 72px;
    border-radius: 36px; background: var(--pill);
    border: 2px solid var(--pill-edge);
    display: flex; align-items: center; padding: 0 40px;
    color: var(--text-muted); font-size: 36px;
  }
  .search-field svg { position: absolute; right: 38px; top: 16px; }

  .sort-tabs {
    position: absolute; left: 0; top: 365px; width: 100%; height: 90px;
    background: linear-gradient(#3a3d42, #2f3237);
    display: flex;
  }
  .sort-tab {
    flex: 1; display: flex; align-items: center; justify-content: center;
    color: var(--text-light); font-size: 40px;
    border-right: 3px solid var(--tab-divider);
  }
  .sort-tab:last-child { border-right: none; }
  .sort-tab.is-active { color: var(--accent); }

  .shelf-panel {
    position: absolute; left: 12px; top: 455px; width: 1116px; height: 920px;
    background: linear-gradient(#3a3d43, var(--shelf-back) 40%, #2e3136);
    box-shadow: inset 0 10px 24px rgba(0,0,0,.5);
  }
  .shelf-ledge {
    position: absolute; left: 0; width: 100%; height: 44px;
    background: linear-gradient(var(--shelf-ledge-top), #44484f 30%, var(--shelf-ledge-bottom));
    box-shadow: 0 12px 18px rgba(0,0,0,.55);
  }
  .shelf-ledge.row-one { top: 392px; }
  .shelf-ledge.row-two { top: 862px; }

  .book {
    position: absolute; width: 210px; height: 340px;
    box-shadow: 6px 6px 12px rgba(0,0,0,.6);
  }
  .row-one-book { top: 64px; }
  .row-two-book { top: 536px; height: 326px; width: 200px; }

  .cover-art { position: absolute; inset: 0; }
  .cover-dictionary { background: linear-gradient(160deg, #2f79c9, #163f7e); }
  .cover-fire { background: radial-gradient(circle at 50% 58%, #f2a02a, #d8461b 45%, #9d2312); }
  .cover-apprentice { background: linear-gradient(#2f78a8, #4d8bb0 45%, #b7a64a); }
  .cover-engines { background: linear-gradient(#6b5a90, #3e3158 70%, #2b2238); }
  .cover-notebook { background: linear-gradient(135deg, #2b2b2b, #5a5a5a 50%, #1e1e1e); }

  .plain-cover { position: absolute; inset: 0; display: flex; flex-direction: column; }
  .plain-cover .label {
    height: 136px; background: var(--cover-cream);
    display: flex; align-items: center; justify-content: center; text-align: center;
    font-family: "Libre Baskerville", Georgia, serif; color: var(--cover-ink);
    font-size: 19px; line-height: 1.25; padding: 60px 12px 6px;
  }
  .plain-cover .label.is-long { font-size: 16px; }
  .plain-cover .body {
    flex: 1; display: flex; justify-content: center; align-items: flex-start; padding-top: 52px;
    font-family: "Libre Baskerville", Georgia, serif; color: #e9e0c8;
    font-size: 12px; letter-spacing: 1px; text-transform: uppercase;
  }
  .plain-cover.maroon .body { background: var(--cover-maroon); }
  .plain-cover.green .body { background: var(--cover-green); }

  .ribbon { position: absolute; right: 6px; top: -6px; }
  .download-badge { position: absolute; right: 10px; bottom: 10px; }

  .screen-foot {
    position: absolute; left: 0; top: 1375px; width: 100%; height: 317px;
    background: linear-gradient(#24262a, #1c1e21);
  }
</style>
</head>
<body>
<main class="app-screen">
  <header class="app-header"><span class="app-name">Shelfwise</span></header>

  <section class="toolbar"></section>
  <svg class="view-list" width="66" height="50" viewBox="0 0 66 50" aria-label="List view">
    <rect x="0" y="0" width="66" height="10" rx="2" fill="var(--icon-muted)"/>
    <rect x="0" y="20" width="66" height="10" rx="2" fill="var(--icon-muted)"/>
    <rect x="0" y="40" width="66" height="10" rx="2" fill="var(--icon-muted)"/>
  </svg>
  <svg class="view-grid" width="42" height="42" viewBox="0 0 42 42" aria-label="Grid view">
    <rect x="0" y="0" width="17" height="17" fill="var(--icon-muted)"/>
    <rect x="25" y="0" width="17" height="17" fill="var(--icon-muted)"/>
    <rect x="0" y="25" width="17" height="17" fill="var(--icon-muted)"/>
    <rect x="25" y="25" width="17" height="17" fill="var(--icon-muted)"/>
  </svg>
  <div class="search-field">Search
    <svg width="38" height="38" viewBox="0 0 38 38" aria-hidden="true">
      <circle cx="15" cy="15" r="11" fill="none" stroke="var(--text-muted)" stroke-width="4"/>
      <line x1="23" y1="23" x2="35" y2="35" stroke="var(--text-muted)" stroke-width="5" stroke-linecap="round"/>
    </svg>
  </div>

  <nav class="sort-tabs">
    <div class="sort-tab is-active">By Author</div>
    <div class="sort-tab">By Recent</div>
    <div class="sort-tab">By Title</div>
  </nav>

  <section class="shelf-panel">
    <div class="shelf-ledge row-one"></div>
    <div class="shelf-ledge row-two"></div>

    <div class="book row-one-book" style="left:84px">
      <div class="cover-art cover-dictionary" role="img" aria-label="Blue dictionary cover"></div>
      <svg class="ribbon" width="44" height="62" viewBox="0 0 44 62"><path d="M0 0H44V62L22 48L0 62Z" fill="var(--ribbon)"/><circle cx="22" cy="24" r="8" fill="var(--ribbon-dot)"/></svg>
    </div>
    <div class="book row-one-book" style="left:337px">
      <div class="cover-art cover-fire" role="img" aria-label="Red and orange novel cover with emblem"></div>
      <svg class="ribbon" width="44" height="62" viewBox="0 0 44 62"><path d="M0 0H44V62L22 48L0 62Z" fill="var(--ribbon)"/><circle cx="22" cy="24" r="8" fill="var(--ribbon-dot)"/></svg>
    </div>
    <div class="book row-one-book" style="left:597px; width:206px">
      <div class="cover-art cover-apprentice" role="img" aria-label="Fantasy novel cover with castle scene"></div>
      <svg class="ribbon" width="44" height="62" viewBox="0 0 44 62"><path d="M0 0H44V62L22 48L0 62Z" fill="var(--ribbon)"/><circle cx="22" cy="24" r="8" fill="var(--ribbon-dot)"/></svg>
      <svg class="download-badge" width="54" height="54" viewBox="0 0 54 54"><circle cx="27" cy="27" r="25" fill="#2a2c30" stroke="#fff" stroke-width="3"/><path d="M27 14V36M18 28L27 37L36 28" fill="none" stroke="#fff" stroke-width="4"/></svg>
    </div>
    <div class="book row-one-book" style="left:854px; width:200px">
      <div class="cover-art cover-engines" role="img" aria-label="Urban fantasy novel cover in purple tones"></div>
      <svg class="ribbon" width="44" height="62" viewBox="0 0 44 62"><path d="M0 0H44V62L22 48L0 62Z" fill="var(--ribbon)"/><circle cx="22" cy="24" r="8" fill="var(--ribbon-dot)"/></svg>
      <svg class="download-badge" width="54" height="54" viewBox="0 0 54 54"><circle cx="27" cy="27" r="25" fill="#2a2c30" stroke="#fff" stroke-width="3"/><path d="M27 14V36M18 28L27 37L36 28" fill="none" stroke="#fff" stroke-width="4"/></svg>
    </div>

    <div class="book row-two-book" style="left:98px">
      <div class="cover-art cover-notebook" role="img" aria-label="Black and white notebook style journal cover"></div>
      <svg class="ribbon" width="44" height="62" viewBox="0 0 44 62"><path d="M0 0H44V62L22 48L0 62Z" fill="var(--ribbon)"/><circle cx="22" cy="24" r="8" fill="var(--ribbon-dot)"/></svg>
    </div>
    <div class="book row-two-book" style="left:337px">
      <div class="plain-cover maroon">
        <div class="label">Harbor Island</div>
        <div class="body">R. L. Marsh</div>
      </div>
      <svg class="ribbon" width="44" height="62" viewBox="0 0 44 62"><path d="M0 0H44V62L22 48L0 62Z" fill="var(--ribbon)"/><circle cx="22" cy="24" r="8" fill="var(--ribbon-dot)"/></svg>
      <svg class="download-badge" width="54" height="54" viewBox="0 0 54 54"><circle cx="27" cy="27" r="25" fill="#2a2c30" stroke="#fff" stroke-width="3"/><path d="M27 14V36M18 28L27 37L36 28" fill="none" stroke="#fff" stroke-width="4"/></svg>
    </div>
    <div class="book row-two-book" style="left:585px">
      <div class="plain-cover green">
        <div class="label">The Tale of Wilton Reed</div>
        <div class="body">Edwin Hale</div>
      </div>
      <svg class="ribbon" width="44" height="62" viewBox="0 0 44 62"><path d="M0 0H44V62L22 48L0 62Z" fill="var(--ribbon)"/><circle cx="22" cy="24" r="8" fill="var(--ribbon-dot)"/></svg>
      <svg class="download-badge" width="54" height="54" viewBox="0 0 54 54"><circle cx="27" cy="27" r="25" fill="#2a2c30" stroke="#fff" stroke-width="3"/><path d="M27 14V36M18 28L27 37L36 28" fill="none" stroke="#fff" stroke-width="4"/></svg>
    </div>
    <div class="book row-two-book" style="left:842px">
      <div class="plain-cover green">
        <div class="label is-long">The Grand Story Shelf Volume 01 Fiction</div>
        <div class="body">Various</div>
      </div>
      <svg class="ribbon" width="44" height="62" viewBox="0 0 44 62"><path d="M0 0H44V62L22 48L0 62Z" fill="var(--ribbon)"/><circle cx="22" cy="24" r="8" fill="var(--ribbon-dot)"/></svg>
      <svg class="download-badge" width="54" height="54" viewBox="0 0 54 54"><circle cx="27" cy="27" r="25" fill="#2a2c30" stroke="#fff" stroke-width="3"/><path d="M27 14V36M18 28L27 37L36 28" fill="none" stroke="#fff" stroke-width="4"/></svg>
    </div>
  </section>

  <div class="screen-foot"></div>
</main>
</body>
</html>
```